Home inspection business! professional look attracting customers just by looks. Read must haves

its a new business I started on my own for home inspections I would like something very professional to give to real estate agents and clients, its going to have my license number on it my business phone number my name my website as well etc on the back side it will be servicing areas and also what kind of services I offer I also have a business card from someone else the way I would like mine to be. I will attach my logo

Home Inspection

listed in nice to haves

• phone number - 555 293 8471
• website- hollowpinecheck.com
• license number #2938475610
• my name Gavin keropulis
• picture of my logo and me on the front
• on the back of the card. stating I am servicing All of New York and Long Island
• also services I will offer will be home inspection -mold inspection -lead inspection -radon inspection -Termite Inspection -Infared Scan.
• and also we provide inspections for single family homes condos co-ops town-homes
• and commercial property
• same colors as the logos and also if you recommend fonts to look like the logo not sure up to you

```html
<!DOCTYPE html>
<html lang="en">
<head>
<meta charset="utf-8">
<title>Hollow Pine Check – Business Card</title>
<link rel="stylesheet" href="https://fonts.googleapis.com/css2?family=Montserrat:wght@400;500;600&display=swap">
<style>
  :root {
    --page: #e9e9e7;
    --card-dark: #2b2b2c;
    --card-light: #ffffff;
    --brand-blue: #4a9ad8;
    --text-grey: #6a6a6a;
    --text-light: #e6e6e6;
  }
  * { box-sizing: border-box; margin: 0; padding: 0; }
  html, body { width: 1200px; height: 900px; overflow: hidden; }
  body {
    background: var(--page);
    font-family: "Montserrat", sans-serif;
    position: relative;
  }
  .card {
    position: absolute;
    left: 250px;
    width: 700px;
    height: 400px;
    box-shadow: 0 6px 18px rgba(0,0,0,0.18);
  }
  .card-back { top: 35px; background: var(--card-dark); }
  .card-front { top: 465px; background: var(--card-light); }

  .brand {
    position: absolute;
    display: flex;
    align-items: center;
    gap: 14px;
    font-weight: 600;
    font-size: 40px;
    letter-spacing: 1px;
    text-transform: uppercase;
    white-space: nowrap;
  }
  .brand-dot {
    width: 22px; height: 22px; border-radius: 50%;
  }
  .card-back .brand { top: 80px; left: 0; right: 0; justify-content: center; color: #ffffff; }
  .card-back .brand-dot { background: #ffffff; }
  .card-front .brand { top: 80px; left: 0; right: 0; justify-content: center; color: var(--text-grey); }
  .card-front .brand-dot { background: var(--text-grey); }

  .service-area {
    position: absolute;
    top: 210px; left: 0; right: 0;
    text-align: center;
    color: var(--brand-blue);
    font-weight: 600;
    font-size: 17px;
    text-transform: uppercase;
  }
  .service-list {
    position: absolute;
    top: 248px; left: 40px; right: 40px;
    text-align: center;
    color: var(--text-light);
    font-size: 15px;
    line-height: 1.55;
  }
  .service-list .sep { color: var(--brand-blue); padding: 0 4px; }

  .owner {
    position: absolute;
    left: 60px; top: 262px;
  }
  .owner-name {
    color: var(--brand-blue);
    font-weight: 600;
    font-size: 27px;
    text-transform: uppercase;
    letter-spacing: 0.5px;
  }
  .owner-license {
    color: var(--text-grey);
    font-size: 17px;
    margin-top: 6px;
    margin-left: 88px;
  }
  .divider {
    position: absolute;
    left: 385px; top: 230px;
    width: 1.5px; height: 112px;
    background: var(--brand-blue);
  }
  .contact-list {
    position: absolute;
    left: 405px; top: 236px;
    list-style: none;
    color: var(--text-grey);
    font-size: 17px;
  }
  .contact-list li {
    display: flex; align-items: center; gap: 9px;
    height: 33px;
  }
  .contact-list svg { width: 15px; height: 15px; fill: var(--brand-blue); flex: none; }
</style>
</head>
<body>

<section class="card card-back">
  <div class="brand"><span class="brand-dot"></span>Hollow Pine Check</div>
  <p class="service-area">Stating I am servicing all of New York and Long Island</p>
  <p class="service-list">
    home inspection <span class="sep">•</span> mold inspection <span class="sep">•</span> lead inspection<br>
    radon inspection <span class="sep">•</span> Termite Inspection <span class="sep">•</span> Infared Scan<br>
    we provide inspections for single family homes condos co-ops town-homes<br>
    and commercial property
  </p>
</section>

<section class="card card-front">
  <div class="brand"><span class="brand-dot"></span>Hollow Pine Check</div>

  <div class="owner">
    <p class="owner-name">Gavin Keropulis</p>
    <p class="owner-license">Lic #2938475610</p>
  </div>

  <div class="divider"></div>

  <ul class="contact-list">
    <li>
      <svg viewBox="0 0 24 24" aria-hidden="true"><path d="M6.6 10.8a15.1 15.1 0 0 0 6.6 6.6l2.2-2.2a1 1 0 0 1 1-.25 11.4 11.4 0 0 0 3.6.57 1 1 0 0 1 1 1V20a1 1 0 0 1-1 1A17 17 0 0 1 3 4a1 1 0 0 1 1-1h3.5a1 1 0 0 1 1 1c0 1.25.2 2.45.57 3.57a1 1 0 0 1-.25 1z"/></svg>
      555 293 8471
    </li>
    <li>
      <svg viewBox="0 0 24 24" aria-hidden="true"><path d="M2 5h20v14H2z M2 5l10 8 10-8" fill="none" stroke="#4a9ad8" stroke-width="2.2"/><path d="M2 5h20l-10 8z"/></svg>
      info@hollowpinecheck.com
    </li>
    <li>
      <svg viewBox="0 0 24 24" aria-hidden="true"><circle cx="12" cy="12" r="9" fill="none" stroke="#4a9ad8" stroke-width="2.2"/><path d="M3 12h18M12 3c3 3 3 15 0 18M12 3c-3 3-3 15 0 18" fill="none" stroke="#4a9ad8" stroke-width="1.6"/></svg>
      www.hollowpinecheck.com
    </li>
  </ul>
</section>

</body>
</html>
```